Banner Ad Design Project

I own a small truck stop. I have an old canopy over the diesel pumps that I am having refurbished. The face of the canopy will be 3 feet tall and about 60 feet long (about 1 meter tall by 20 meters long) in white.

The name of my Truck Stop is "Halvern Truck Stop" I would like to design a banner/logo that would flow across the front of this Face on the canopy... I'm imagining something red, white and blue, with stars and HALVERN TRUCK STOP designed into it...

We are basically a small gas station/truck stop.

Target Market(s)

Truckers ....

Industry/Entity Type

Gas Station

```html
<!DOCTYPE html>
<html lang="en">
<head>
<meta charset="utf-8">
<title>Halvern Truck Stop – Canopy Banner</title>
<link rel="stylesheet" href="https://fonts.googleapis.com/css2?family=Roboto+Condensed:wght@800&display=swap">
<style>
  :root {
    --banner-red: #d0262f;
    --banner-blue: #1f4fa3;
    --banner-white: #ffffff;
    --frame-line: #3a3a3a;
  }
  html, body {
    margin: 0;
    padding: 0;
    width: 1200px;
    height: 108px;
    overflow: hidden;
    background: var(--banner-white);
  }
  .canopy-banner {
    display: block;
    width: 1200px;
    height: 108px;
  }
  .canopy-frame {
    fill: var(--banner-white);
    stroke: var(--frame-line);
    stroke-width: 1.2;
  }
  .stripe-fill { fill: var(--banner-red); }
  .stripe-edge { fill: var(--banner-blue); }
  .brand-name {
    font-family: "Roboto Condensed", "Arial Narrow", sans-serif;
    font-weight: 800;
    font-size: 62px;
    fill: var(--banner-red);
  }
  .band-label {
    font-family: "Roboto Condensed", "Arial Narrow", sans-serif;
    font-weight: 800;
    font-size: 20px;
    letter-spacing: 1px;
    fill: var(--banner-white);
  }
</style>
</head>
<body>
<svg class="canopy-banner" viewBox="0 0 1200 108" xmlns="http://www.w3.org/2000/svg" role="img" aria-label="Halvern Truck Stop canopy banner">
  <!-- canopy face -->
  <rect class="canopy-frame" x="7" y="24" width="1186" height="58"/>

  <!-- left stripe -->
  <rect class="stripe-edge" x="7" y="40" width="52" height="28"/>
  <rect class="stripe-fill" x="7" y="43" width="49" height="22"/>

  <!-- name -->
  <text class="brand-name" x="70" y="77" textLength="236" lengthAdjust="spacingAndGlyphs">HALVERN</text>

  <!-- main band -->
  <polygon class="stripe-edge" points="318,40 1193,40 1193,68 328,68"/>
  <polygon class="stripe-fill" points="324,43 1193,43 1193,65 332,65"/>
  <text class="band-label" x="350" y="62">TRUCK STOP</text>
</svg>
</body>
</html>
```